Pop punk gig poster design!

In need of an amazing poster design for a gig We are organising, the genre is pop punk, and will be an all ages gig. I need to it bold, random and capture the eye of any bypasses, and make people want to go to the gig just because the poster is awesome! The event will be called "A glimpse of neon" and will consist of three bands and an acoustic set to open. All the bands are full of energy and create an unreal ambiance during there shows, I would like to capture that in the poster. Open to anything spectacular, the sky is the limit.

• I need to have the name of the event "A Glimpse Of Neon"
Band names(in this order):
-Fold the Lantern
-Velvet Orchard
-Gemwick's Oar
-Lunetta Pribble

Date: Saturday 10th November 2012
Time: 5:15pm
Venue: The Quill, 47 Marrowfen street, West End, QLD 4101
Ticket price: $10+bf online
$15 at the door.
Free BBQ

```html
<!DOCTYPE html>
<html lang="en">
<head>
<meta charset="utf-8">
<title>A Glimpse Of Neon – Gig Poster</title>
<link rel="stylesheet" href="https://fonts.googleapis.com/css2?family=Cinzel:wght@400&family=Pathway+Gothic+One&display=swap">
<style>
  :root {
    --ink: #000000;
    --neon: #2dff2d;
    --neon-soft: #1fc41f;
    --smoke: #0b3a0b;
    --glow: rgba(45, 255, 45, 0.55);
  }
  html, body {
    margin: 0;
    padding: 0;
    width: 800px;
    height: 1200px;
    overflow: hidden;
    background: var(--ink);
  }
  .poster {
    display: block;
    width: 800px;
    height: 1200px;
  }
  .poster text {
    fill: var(--neon);
    filter: drop-shadow(0 0 4px var(--glow));
  }
  .event-title, .event-time, .tickets, .free-bbq {
    font-family: "Cinzel", serif;
  }
  .event-date, .event-venue, .band {
    font-family: "Pathway Gothic One", sans-serif;
  }
  .event-title { font-size: 60px; }
  .event-time { font-size: 42px; }
  .event-date { font-size: 42px; }
  .event-venue { font-size: 58px; }
  .band { font-size: 54px; }
  .tickets { font-size: 40px; }
  .free-bbq { font-size: 72px; }
</style>
</head>
<body>
<svg class="poster" viewBox="0 0 800 1200" xmlns="http://www.w3.org/2000/svg">
  <defs>
    <radialGradient id="smoke-fill" cx="50%" cy="54%" r="55%">
      <stop offset="0%" stop-color="#000"/>
      <stop offset="38%" stop-color="#031503"/>
      <stop offset="55%" stop-color="var(--smoke)"/>
      <stop offset="75%" stop-color="#051d05"/>
      <stop offset="100%" stop-color="#000"/>
    </radialGradient>
    <radialGradient id="ring-fill" cx="50%" cy="50%" r="50%">
      <stop offset="80%" stop-color="#0a5a0a"/>
      <stop offset="90%" stop-color="var(--neon-soft)"/>
      <stop offset="100%" stop-color="#0a5a0a"/>
    </radialGradient>
    <filter id="ring-glow" x="-20%" y="-20%" width="140%" height="140%">
      <feGaussianBlur stdDeviation="6"/>
    </filter>
  </defs>

  <rect width="800" height="1200" fill="var(--ink)"/>

  <ellipse class="smoke" role="img" aria-label="Green neon smoke swirling around the ring"
           cx="400" cy="653" rx="420" ry="380" fill="url(#smoke-fill)"/>

  <g class="rune-ring" role="img" aria-label="Glowing green ring of runes">
    <circle cx="400" cy="653" r="300" fill="none" stroke="var(--neon)" stroke-width="58" opacity="0.45" filter="url(#ring-glow)"/>
    <path d="M400 326a327 327 0 1 1 0 654a327 327 0 1 1 0-654z M400 380a273 273 0 1 0 0 546a273 273 0 1 0 0-546z"
          fill="url(#ring-fill)" fill-rule="evenodd" opacity="0.8"/>
    <circle cx="400" cy="653" r="327" fill="none" stroke="var(--neon)" stroke-width="3"/>
    <circle cx="400" cy="653" r="273" fill="none" stroke="var(--neon)" stroke-width="3"/>
  </g>

  <text class="event-title" x="400" y="85" text-anchor="middle" textLength="700" lengthAdjust="spacingAndGlyphs">A GLIMPSE OF NEON</text>
  <text class="event-date" x="40" y="174" textLength="517" lengthAdjust="spacingAndGlyphs">SATURDAY 10TH OF NOVEMBER 2012</text>
  <text class="event-time" x="607" y="174" textLength="153" lengthAdjust="spacingAndGlyphs">5:15PM</text>
  <text class="event-venue" x="27" y="287" textLength="740" lengthAdjust="spacingAndGlyphs">THE QUILL, 47 MARROWFEN STREET, WEST END, QLD 4101</text>

  <g class="line-up">
    <text class="band" x="400" y="549" text-anchor="middle" textLength="270" lengthAdjust="spacingAndGlyphs">FOLD THE LANTERN</text>
    <text class="band" x="400" y="634" text-anchor="middle" textLength="395" lengthAdjust="spacingAndGlyphs">VELVET ORCHARD</text>
    <text class="band" x="400" y="718" text-anchor="middle" textLength="395" lengthAdjust="spacingAndGlyphs">GEMWICK'S OAR</text>
    <text class="band" x="400" y="803" text-anchor="middle" textLength="396" lengthAdjust="spacingAndGlyphs">LUNETTA PRIBBLE</text>
  </g>

  <g class="ticket-info">
    <text class="tickets" x="7" y="1020" textLength="200" lengthAdjust="spacingAndGlyphs">TICKETS</text>
    <text class="tickets" x="27" y="1090" textLength="237" lengthAdjust="spacingAndGlyphs">$10  ONLINE</text>
    <text class="tickets" x="27" y="1157" textLength="395" lengthAdjust="spacingAndGlyphs">$15 AT THE DOOR</text>
  </g>

  <text class="free-bbq" x="483" y="1157" textLength="304" lengthAdjust="spacingAndGlyphs">FREE BBQ</text>
</svg>
</body>
</html>
```